Completely Coded Dog Community Website - Mobile Centric & Highly Responsive

We need a completely coded design based in Wordpress CMS that is designed with mobile in mind first! I would like to carry over the style of our current website (brightkennels.c0m) into the design of the responsive website. In addition, please only submit designs if you provide high quality admin support, as the winning design will likely be hired to provide monthly support forward at $100/month (SEO skill set valued). Also am looking for a quote on an iphone and android app so please submit designs only if you have capability to create the highest quality apps. No cheap looking template submissions please...will need form, chat, sign in and e-commerce integration. I have vector files if needed for website.
Updates

Project Deadline Extended
Reason: Want to see more mobile friendly, modern designs and responses to willingness for web admin support going forward. Thanks

Target Market(s)

Adults based in the USA aged 25-50 that own dogs

Industry/Entity Type

E-Commerce

Requirements
Must have
• Pages:
Home Page
About Us
Contact Us
Dog Deals
Videos
Photos
Health
Training
Breeds
Ask the Dog Expert
Dog Product Reviews
Dog Stories
Dog Friendly Travel
Dog Care
Contests
Nice to have
• SEO
Metatags
Unique page layouts
Social integration to our social media accounts
Social API logins
Should not have
• Cheap template look
Not consistent with previous color scheme
Different logo than our current options

```html
<!DOCTYPE html>
<html lang="en">
<head>
<meta charset="utf-8">
<title>BrightKennels – Dog Community</title>
<link rel="stylesheet" href="https://fonts.googleapis.com/css2?family=Signika:wght@400;600;700&family=Open+Sans:wght@400;600&display=swap">
<style>
  :root {
    --sky-top: #4fb3e2;
    --sky-bottom: #a6dcf3;
    --meadow: #c3e574;
    --meadow-edge: #b2d95e;
    --teal: #2f86a7;
    --nav-blue: #5bc3e8;
    --nav-blue-dark: #3aa6cf;
    --ink: #222;
    --footer-ink: #1e2a10;
    --white: #fff;
    --footer-top: #b5d872;
    --footer-bottom: #8fb749;
    --field: #86a93c;
    --field-text: #d9ebb2;
    --button-light: #cfe9f5;
    --bar: #2c7187;
    --chat: #4cbfe6;
  }
  * { box-sizing: border-box; margin: 0; padding: 0; }
  html, body { width: 1156px; height: 1200px; overflow: hidden; }
  body {
    position: relative;
    background: var(--white);
    font-family: "Open Sans", Arial, sans-serif;
    color: var(--ink);
  }

  /* Sky header */
  .sky {
    position: absolute; left: 0; top: 0; width: 1156px; height: 360px;
    background: linear-gradient(180deg, var(--sky-top) 0%, var(--sky-bottom) 100%);
  }
  .sky::before {
    content: ""; position: absolute; left: 0; right: 0; top: 0; height: 5px;
    background: #2fa6d6;
  }
  .meadow {
    position: absolute; left: 0; top: 352px; width: 1156px; height: 212px;
    background: var(--meadow);
  }
  .meadow-top {
    position: absolute; left: 0; top: 338px; width: 1156px; height: 16px;
    background: radial-gradient(ellipse 34px 16px at 34px 16px, var(--meadow) 98%, transparent 100%) repeat-x;
    background-size: 68px 16px;
  }
  .meadow-bottom {
    position: absolute; left: 0; top: 562px; width: 1156px; height: 14px;
    background: radial-gradient(ellipse 18px 14px at 18px 0, var(--meadow) 96%, var(--meadow-edge) 98%, transparent 100%) repeat-x;
    background-size: 36px 14px;
  }

  /* Brand */
  .brand {
    position: absolute; left: 244px; top: 28px;
    display: flex; align-items: center; gap: 7px;
  }
  .brand-mark { width: 28px; height: 28px; border-radius: 50%; background: #f5a623; }
  .brand-name {
    font-family: "Signika", Arial, sans-serif; font-weight: 700;
    font-size: 22px; color: #1f5f86; letter-spacing: -0.3px;
  }

  /* Social strip */
  .social { position: absolute; left: 751px; top: 0; display: flex; gap: 2px; }
  .social span {
    width: 26px; height: 29px; background: #3fb3e0;
    display: flex; align-items: center; justify-content: center;
  }
  .social i { width: 12px; height: 12px; border-radius: 50%; background: var(--white); display: block; }

  /* Navigation */
  .nav { position: absolute; top: 49px; left: 432px; display: flex; gap: 4px; }
  .nav a {
    display: block; height: 26px; line-height: 25px; padding: 0 12px;
    font-family: "Signika", Arial, sans-serif; font-size: 14px; font-weight: 600;
    color: var(--white); text-decoration: none; border-radius: 4px;
    background: linear-gradient(180deg, #6ccdef, var(--nav-blue-dark));
    box-shadow: inset 0 -2px 0 rgba(0,0,0,.12);
  }
  .nav a.is-current { background: linear-gradient(180deg, #c9ec85, #a5d658); }

  /* Slider */
  .slider {
    position: absolute; left: 238px; top: 96px; width: 679px; height: 305px;
    border: 2px solid #7ec9e8; border-radius: 4px;
    background: rgba(255,255,255,.35); padding: 6px;
  }
  .slide {
    width: 100%; height: 100%;
    background: linear-gradient(180deg, #4f8a2c 0%, #8fbb4e 30%, #e2bd82 55%, #d6a45e 80%, #b97a3a 100%);
  }
  .slider-arrow {
    position: absolute; top: 140px; width: 22px; height: 22px; border-radius: 50%;
    background: rgba(90,90,90,.7); display: flex; align-items: center; justify-content: center;
  }
  .slider-arrow.prev { left: 8px; }
  .slider-arrow.next { right: 8px; }

  /* Feature blurbs */
  .feature { position: absolute; width: 215px; }
  .feature-icon { position: absolute; left: 0; top: 0; width: 34px; height: 34px; border-radius: 4px; }
  .feature-title {
    position: absolute; top: 22px; font-family: "Signika", Arial, sans-serif;
    font-size: 16px; font-weight: 600; color: var(--teal); white-space: nowrap;
  }
  .feature-text {
    position: absolute; top: 48px; width: 212px; font-size: 10.5px; line-height: 15px;
    text-indent: 38px; text-align: justify; color: var(--ink);
  }
  .learn-more {
    position: absolute; top: 112px; font-family: "Signika", Arial, sans-serif;
    font-size: 12px; font-weight: 600; color: var(--teal); text-decoration: none;
  }

  .ad-frame {
    position: absolute; left: 725px; top: 416px; width: 172px; height: 132px;
    background: var(--white); border: 1px solid #9ab; padding: 4px;
    box-shadow: 0 1px 3px rgba(0,0,0,.2);
  }
  .ad-frame div { width: 100%; height: 100%; background: linear-gradient(135deg, #2c2622 0%, #4a3f37 50%, #1b1714 100%); }

  /* Topic cards */
  .carousel-nav { position: absolute; left: 876px; top: 594px; display: flex; gap: 4px; }
  .carousel-nav span {
    width: 16px; height: 15px; border: 1px solid #5a9cc0; border-radius: 3px;
    background: #eef7fc; display: flex; align-items: center; justify-content: center;
  }
  .card { position: absolute; top: 621px; width: 150px; text-align: center; }
  .card-photo {
    width: 150px; height: 135px; border: 1px solid #6f9fc4; padding: 4px; background: var(--white);
  }
  .card-photo div { width: 100%; height: 100%; }
  .card-title {
    margin-top: 11px; font-family: "Signika", Arial, sans-serif; font-size: 14px;
    font-weight: 600; color: var(--teal);
  }
  .card-text {
    margin: 1px -8px 0; font-size: 9.4px; line-height: 14px; letter-spacing: -0.15px;
    white-space: nowrap;
  }
  .more-btn {
    display: block; margin: 18px auto 0; width: 58px; height: 20px; line-height: 18px;
    font-size: 11px; color: #3a6b80; border: 1px solid #8cb5c9; border-radius: 2px;
    background: linear-gradient(180deg, #e6f4fb, #c6e3f1); text-decoration: none;
  }

  /* Meadow scene */
  .meadow-scene {
    position: absolute; left: 0; top: 858px; width: 1156px; height: 124px;
    background: linear-gradient(180deg, #ffffff 0%, #c8e8f2 28%, #9fcfe0 40%, #a7d46a 55%, #6fae32 80%, #8dbf45 100%);
  }

  /* Footer */
  .footer {
    position: absolute; left: 0; top: 980px; width: 1156px; height: 191px;
    background: linear-gradient(180deg, var(--footer-top) 0%, #a2c85e 60%, var(--footer-bottom) 100%);
  }
  .footer-heading {
    position: absolute; top: 990px; font-family: "Signika", Arial, sans-serif;
    font-size: 13px; font-weight: 700; color: var(--footer-ink);
  }
  .popular { position: absolute; top: 1018px; width: 158px; list-style: none; }
  .popular li {
    position: relative; padding-left: 22px; font-size: 10px; line-height: 12px;
    color: var(--footer-ink); margin-bottom: 4px;
  }
  .popular li svg { position: absolute; left: 0; top: 1px; }
  .field {
    position: absolute; background: var(--field); color: var(--field-text);
    font-size: 10px; padding: 2px 6px; border: 1px solid #7a9a35;
  }
  .btn-light {
    position: absolute; height: 21px; line-height: 19px; text-align: center;
    font-size: 10.5px; color: #3a6b80; border: 1px solid #8cb5c9;
    background: linear-gradient(180deg, #eef8fc, var(--button-light));
  }
  .newsletter-note { position: absolute; left: 768px; top: 1016px; font-size: 10px; color: var(--footer-ink); }
  .footer-brand {
    position: absolute; left: 772px; top: 1094px; display: flex; align-items: center; gap: 6px;
  }
  .footer-brand .brand-mark { width: 24px; height: 24px; background: #6f7a73; }
  .footer-brand .brand-name { font-size: 20px; color: #3b4a3f; }
  .chat-now {
    position: absolute; left: 764px; top: 1145px; width: 152px; height: 26px;
    background: linear-gradient(180deg, #6dd0f0, var(--chat)); color: var(--white);
    font-family: "Signika", Arial, sans-serif; font-weight: 700; font-size: 14px;
    display: flex; align-items: center; justify-content: center; gap: 8px;
  }
  .bottom-bar {
    position: absolute; left: 0; top: 1171px; width: 1156px; height: 29px;
    background: var(--bar); color: var(--white); font-size: 10.5px;
  }
  .bottom-bar p { position: absolute; left: 257px; top: 7px; }
</style>
</head>
<body>

<div class="sky"></div>
<div class="meadow-top"></div>
<div class="meadow"></div>
<div class="meadow-bottom"></div>

<div class="social" aria-label="Search and social links">
  <span><svg width="13" height="13" viewBox="0 0 13 13"><circle cx="5.5" cy="5.5" r="4" fill="none" stroke="#fff" stroke-width="2"/><line x1="8.5" y1="8.5" x2="12" y2="12" stroke="#fff" stroke-width="2"/></svg></span>
  <span><i></i></span>
  <span><i></i></span>
  <span><i></i></span>
  <span><i></i></span>
  <span><svg width="12" height="12" viewBox="0 0 12 12"><path d="M6 0v12M0 6h12" stroke="#fff" stroke-width="2"/></svg></span>
</div>

<div class="brand">
  <span class="brand-mark"></span>
  <span class="brand-name">BrightKennels</span>
</div>

<nav class="nav">
  <a href="#" class="is-current">Home</a>
  <a href="#">About Us</a>
  <a href="#">Dog Deals</a>
  <a href="#">Videos</a>
  <a href="#">Photos</a>
  <a href="#">Breeds</a>
  <a href="#">Contact</a>
</nav>

<div class="slider">
  <div class="slide" role="img" aria-label="Photo of three golden retriever puppies resting paws on a wooden rail"></div>
  <span class="slider-arrow prev"><svg width="8" height="10" viewBox="0 0 8 10"><path d="M6 1L2 5l4 4" fill="none" stroke="#fff" stroke-width="2"/></svg></span>
  <span class="slider-arrow next"><svg width="8" height="10" viewBox="0 0 8 10"><path d="M2 1l4 4-4 4" fill="none" stroke="#fff" stroke-width="2"/></svg></span>
</div>

<section class="feature" style="left:241px;top:413px;">
  <div class="feature-icon" role="img" aria-label="Portrait of the dog expert" style="background:linear-gradient(180deg,#d9d4cf,#4f5b66);"></div>
  <h3 class="feature-title" style="left:45px;">Ask the Dog Expert</h3>
  <p class="feature-text" style="left:7px;">Temporibus autem quibusdam et aut officiis debitis aut rerum necessitatibus saepe eveniet ut et voluptates...</p>
  <a class="learn-more" href="#" style="left:7px;">Learn More</a>
</section>

<section class="feature" style="left:472px;top:413px;">
  <div class="feature-icon" role="img" aria-label="Small image of a puppy with a toy" style="background:linear-gradient(180deg,#e6c995,#9a6b2f);"></div>
  <h3 class="feature-title" style="left:50px;">Dog Product Reviews</h3>
  <p class="feature-text" style="left:7px;">Itaque earum rerum hic tenetur a sapiente delectus, ut aut reiciendis maiores alias consequatur ...</p>
  <a class="learn-more" href="#" style="left:7px;">Learn More</a>
</section>

<div class="ad-frame"><div role="img" aria-label="Animal welfare campaign poster showing a man holding a pug"></div></div>

<div class="carousel-nav">
  <span><svg width="6" height="8" viewBox="0 0 6 8"><path d="M5 1L2 4l3 3" fill="none" stroke="#2f6f95" stroke-width="1.5"/></svg></span>
  <span><svg width="6" height="8" viewBox="0 0 6 8"><path d="M1 1l3 3-3 3" fill="none" stroke="#2f6f95" stroke-width="1.5"/></svg></span>
</div>

<article class="card" style="left:240px;">
  <div class="card-photo"><div role="img" aria-label="Photo of a woman grooming a small terrier" style="background:linear-gradient(135deg,#c9455a,#b98a5f 60%,#e7d3b6);"></div></div>
  <h4 class="card-title">Health</h4>
  <p class="card-text">Nemo enim ipsam voluptatem quia<br>voluptas sit aspernatur aut odit aut</p>
  <a class="more-btn" href="#">More</a>
</article>

<article class="card" style="left:415px;">
  <div class="card-photo"><div role="img" aria-label="Photo of a puppy and a rabbit on a wooden chair" style="background:linear-gradient(135deg,#6a9a3a,#d7a768 50%,#8b5a2b);"></div></div>
  <h4 class="card-title">Dog Stories</h4>
  <p class="card-text">Nemo enim ipsam voluptatem quia<br>voluptas sit aspernatur aut odit aut</p>
  <a class="more-btn" href="#">More</a>
</article>

<article class="card" style="left:590px;">
  <div class="card-photo"><div role="img" aria-label="Photo of a boy holding a small dog in a car" style="background:linear-gradient(135deg,#cdb9a0,#e9d7c6 45%,#4b8fb0);"></div></div>
  <h4 class="card-title">Dog Friendly Travel</h4>
  <p class="card-text">Nemo enim ipsam voluptatem quia<br>voluptas sit aspernatur aut odit aut</p>
  <a class="more-btn" href="#">More</a>
</article>

<article class="card" style="left:765px;">
  <div class="card-photo"><div role="img" aria-label="Photo of a puppy with a tennis ball on grass" style="background:linear-gradient(180deg,#8c7a5c,#efe6d6 45%,#5e9a2e);"></div></div>
  <h4 class="card-title">Training</h4>
  <p class="card-text">Nemo enim ipsam voluptatem quia<br>voluptas sit aspernatur aut odit aut</p>
  <a class="more-btn" href="#">More</a>
</article>

<div class="meadow-scene" role="img" aria-label="Illustrated meadow with mountains, daisies, a man walking a dog and several puppies in the grass"></div>

<footer class="footer"></footer>

<h5 class="footer-heading" style="left:241px;">Most Popular</h5>
<ul class="popular" style="left:241px;">
  <li><svg width="11" height="11" viewBox="0 0 11 11"><circle cx="5.5" cy="7.5" r="2.6" fill="#1e2a10"/><circle cx="2" cy="4" r="1.3" fill="#1e2a10"/><circle cx="4.3" cy="2" r="1.3" fill="#1e2a10"/><circle cx="6.8" cy="2" r="1.3" fill="#1e2a10"/><circle cx="9" cy="4" r="1.3" fill="#1e2a10"/></svg>Demoralized by the charms consequat.</li>
  <li><svg width="11" height="11" viewBox="0 0 11 11"><circle cx="5.5" cy="7.5" r="2.6" fill="#1e2a10"/><circle cx="2" cy="4" r="1.3" fill="#1e2a10"/><circle cx="4.3" cy="2" r="1.3" fill="#1e2a10"/><circle cx="6.8" cy="2" r="1.3" fill="#1e2a10"/><circle cx="9" cy="4" r="1.3" fill="#1e2a10"/></svg>Praising pain was born aspernatur.</li>
  <li><svg width="11" height="11" viewBox="0 0 11 11"><circle cx="5.5" cy="7.5" r="2.6" fill="#1e2a10"/><circle cx="2" cy="4" r="1.3" fill="#1e2a10"/><circle cx="4.3" cy="2" r="1.3" fill="#1e2a10"/><circle cx="6.8" cy="2" r="1.3" fill="#1e2a10"/><circle cx="9" cy="4" r="1.3" fill="#1e2a10"/></svg>Exercitation ullamco laboris.</li>
  <li><svg width="11" height="11" viewBox="0 0 11 11"><circle cx="5.5" cy="7.5" r="2.6" fill="#1e2a10"/><circle cx="2" cy="4" r="1.3" fill="#1e2a10"/><circle cx="4.3" cy="2" r="1.3" fill="#1e2a10"/><circle cx="6.8" cy="2" r="1.3" fill="#1e2a10"/><circle cx="9" cy="4" r="1.3" fill="#1e2a10"/></svg>Demoralized by the charms laboris.</li>
  <li><svg width="11" height="11" viewBox="0 0 11 11"><circle cx="5.5" cy="7.5" r="2.6" fill="#1e2a10"/><circle cx="2" cy="4" r="1.3" fill="#1e2a10"/><circle cx="4.3" cy="2" r="1.3" fill="#1e2a10"/><circle cx="6.8" cy="2" r="1.3" fill="#1e2a10"/><circle cx="9" cy="4" r="1.3" fill="#1e2a10"/></svg>Praising pain was born vel eum.</li>
</ul>
<ul class="popular" style="left:418px;">
  <li><svg width="11" height="11" viewBox="0 0 11 11"><circle cx="5.5" cy="7.5" r="2.6" fill="#1e2a10"/><circle cx="2" cy="4" r="1.3" fill="#1e2a10"/><circle cx="4.3" cy="2" r="1.3" fill="#1e2a10"/><circle cx="6.8" cy="2" r="1.3" fill="#1e2a10"/><circle cx="9" cy="4" r="1.3" fill="#1e2a10"/></svg>Exercitation ullamco laboris vel eum</li>
  <li><svg width="11" height="11" viewBox="0 0 11 11"><circle cx="5.5" cy="7.5" r="2.6" fill="#1e2a10"/><circle cx="2" cy="4" r="1.3" fill="#1e2a10"/><circle cx="4.3" cy="2" r="1.3" fill="#1e2a10"/><circle cx="6.8" cy="2" r="1.3" fill="#1e2a10"/><circle cx="9" cy="4" r="1.3" fill="#1e2a10"/></svg>Praising pain was born aspernatur.</li>
  <li><svg width="11" height="11" viewBox="0 0 11 11"><circle cx="5.5" cy="7.5" r="2.6" fill="#1e2a10"/><circle cx="2" cy="4" r="1.3" fill="#1e2a10"/><circle cx="4.3" cy="2" r="1.3" fill="#1e2a10"/><circle cx="6.8" cy="2" r="1.3" fill="#1e2a10"/><circle cx="9" cy="4" r="1.3" fill="#1e2a10"/></svg>Demoralized by the charms laboris.</li>
  <li><svg width="11" height="11" viewBox="0 0 11 11"><circle cx="5.5" cy="7.5" r="2.6" fill="#1e2a10"/><circle cx="2" cy="4" r="1.3" fill="#1e2a10"/><circle cx="4.3" cy="2" r="1.3" fill="#1e2a10"/><circle cx="6.8" cy="2" r="1.3" fill="#1e2a10"/><circle cx="9" cy="4" r="1.3" fill="#1e2a10"/></svg>Praising pain was born vel eum.</li>
  <li><svg width="11" height="11" viewBox="0 0 11 11"><circle cx="5.5" cy="7.5" r="2.6" fill="#1e2a10"/><circle cx="2" cy="4" r="1.3" fill="#1e2a10"/><circle cx="4.3" cy="2" r="1.3" fill="#1e2a10"/><circle cx="6.8" cy="2" r="1.3" fill="#1e2a10"/><circle cx="9" cy="4" r="1.3" fill="#1e2a10"/></svg>Exercitation ullamco laboris vel eum.</li>
</ul>

<h5 class="footer-heading" style="left:592px;">Quick Contact</h5>
<div class="field" style="left:592px;top:1018px;width:146px;height:19px;">Name...</div>
<div class="field" style="left:592px;top:1040px;width:146px;height:19px;">Email...</div>
<div class="field" style="left:592px;top:1061px;width:146px;height:41px;">Message...</div>
<div class="btn-light" style="left:678px;top:1112px;width:60px;">Submit</div>

<h5 class="footer-heading" style="left:768px;">Newsletter</h5>
<p class="newsletter-note">Subscribe to our Newsletter</p>
<div class="field" style="left:763px;top:1035px;width:153px;height:21px;padding-top:4px;">Email...</div>
<div class="btn-light" style="left:850px;top:1066px;width:66px;">Subscribe</div>
<div class="footer-brand">
  <span class="brand-mark"></span>
  <span class="brand-name">BrightKennels</span>
</div>
<div class="chat-now">
  <svg width="18" height="14" viewBox="0 0 18 14"><ellipse cx="9" cy="6" rx="8" ry="5.5" fill="#1e6f93"/><path d="M4 10l-1 4 5-3z" fill="#1e6f93"/></svg>
  Chat Now
</div>

<div class="bottom-bar"><p>© copyright information here</p></div>

</body>
</html>
```